CrumbValet Retail box packaging- 25cm x 10cm x10cm

Retail Packaging. For: Natural Peanut Butter Electric Mixer.<br/>THE CRUMB VALET- the natural peanut butter mixer.<br/>25cm x 10 x10. Full colour . White , cobalt grey and turquoise or green accents.<br/>Product description:<br/>New mixer customized for mixing in store bought natural nut butters that naturally separate on the shelf.—- oil above and nuts below. <br/>Making.the messy mix-in an absolute breeze! <br/>3 speed high torque custom motor. With unique 2mm Stainless Steel hook designed to draw oil down and force nuts up into the vortex...without displacing the oil and mixing it perfectly from top to bottom. Quick release buttons and dishwasher safe<br/>No Mess-No Waste -Better Taste<br/>Mix once at room temperature then refrigerate and Done.<br/>Would love to include graphics showing all nuts with leaves to show it’s perfect for all types of nut butters.<br/>Peanut- Almond-Cashew- Macadamia- Hazelnut- Pistachio<br/><br/>I am waiting for final prototype photography. Currently working with CAD drawings. But want to get packaging going. <br/>Mixer will be black with a Stainless Steel not the gold/black as shown. We will drop in product photo later.<br/>Right side of box should be for healthy colourful peanut butter snack images. Ie red apples and peanut butter. I saw some beautiful stock photo images. Will pay for those images above sketch guild cost. <br/>I will also upload a high res design file of my logo.<br/><br/>I am happy to provide a word document with all necessary text. Or you can work with the above text and I’ll add or tweak text as needed, once the look is established. Please let me know your preference.<br/><br/>

Target Market(s)

North American (Canadian and US) moms. Needs to look high quality. German style quality and image. Like Torvel and Homequill, Pantrovex,

Colors
0692cd
afd34e

Requirements
Must have
• Adding Oily jar of peanut butter on front of box with mixer lowering into jar. Please cover or hide any brand names.

```html
<!DOCTYPE html>
<html lang="en">
<head>
<meta charset="utf-8">
<title>Crumb Valet – Retail Box Panels</title>
<link rel="stylesheet" href="https://fonts.googleapis.com/css2?family=Barlow+Condensed:wght@400;500;600&family=Barlow:wght@400;500;600&display=swap">
<style>
  :root{
    --slate:#3e4b55;
    --slate-dark:#34404a;
    --slate-soft:#4a5862;
    --teal:#3cb5ab;
    --teal-soft:rgba(60,181,171,.28);
    --panel-light:#ecedee;
    --ink:#3b4752;
    --white:#ffffff;
    --stage:#dfe3e4;
    --photo-warm:#c9b79c;
    --photo-toast:#b98a52;
  }
  *{box-sizing:border-box;margin:0;padding:0}
  html,body{width:1200px;height:929px;overflow:hidden}
  body{background:var(--stage);font-family:"Barlow",sans-serif;color:var(--ink);position:relative}

  .box-sheet{position:absolute;left:135px;top:90px;display:flex;gap:15px}
  .panel{width:300px;height:750px;position:relative;overflow:hidden}

  /* Nut list side */
  .panel--nuts{background:var(--slate)}
  .nuts-frame{position:absolute;inset:14px;border:1.5px solid var(--teal)}
  .nuts-title{position:absolute;top:40px;left:0;right:0;text-align:center;font-family:"Barlow Condensed",sans-serif;font-weight:500;font-size:27px;line-height:1.25;color:var(--white)}
  .nut-list{position:absolute;top:140px;left:40px;right:40px;list-style:none}
  .nut-item{height:96px;border-top:1.5px solid var(--teal);display:flex;flex-direction:column;align-items:center;justify-content:center;gap:7px}
  .nut-icon{width:42px;height:42px;border-radius:50%;background:radial-gradient(circle at 40% 35%,var(--teal-soft) 0%,rgba(60,181,171,.14) 60%,rgba(60,181,171,.06) 100%)}
  .nut-name{font-family:"Barlow Condensed",sans-serif;font-size:20px;color:#d9e0e3}

  /* Front panel */
  .panel--front{background:var(--panel-light)}
  .brand{position:absolute;top:46px;left:0;right:0;display:flex;align-items:center;justify-content:center;gap:10px}
  .brand-square{width:22px;height:22px;background:var(--slate)}
  .brand-name{font-family:"Barlow",sans-serif;font-weight:500;font-size:26px;letter-spacing:1px;color:var(--slate)}
  .product-shot{position:absolute;left:34px;top:140px;width:120px;height:570px;border-radius:10px;
    background:
      linear-gradient(180deg,
        rgba(236,237,238,0) 0%,
        #a9afb0 4%,
        #8c9394 22%,
        #7b8283 38%,
        #3a4044 44%,
        #2c3134 56%,
        #7d8485 62%,
        #9aa0a1 74%,
        #d3d6d7 80%,
        #c4c7c8 100%)}
  .badges{position:absolute;left:175px;top:215px;display:flex;flex-direction:column;gap:40px}
  .badge{width:92px;height:92px}
  .claims{position:absolute;right:22px;bottom:95px;display:flex;flex-direction:column;gap:8px;align-items:flex-end}
  .claim{background:var(--teal);color:var(--slate-dark);font-family:"Barlow Condensed",sans-serif;font-weight:500;font-size:19px;width:112px;text-align:center;padding:3px 0;border-radius:14px}

  /* Photo side */
  .panel--snack{background:linear-gradient(155deg,#d8cab4 0%,var(--photo-warm) 45%,var(--photo-toast) 100%)}
  .snack-photo{position:absolute;inset:0}
  .serving-note{position:absolute;left:58px;top:320px;width:184px;height:170px;background:var(--white);outline:1px solid var(--white);outline-offset:6px;display:flex;align-items:center;justify-content:center;text-align:center;font-family:"Barlow",sans-serif;font-size:18px;line-height:1.4;color:var(--ink);padding:12px}
</style>
</head>
<body>
<main class="box-sheet">

  <section class="panel panel--nuts">
    <div class="nuts-frame"></div>
    <h2 class="nuts-title">Perfect For All Types<br>Of Nut Butters</h2>
    <ul class="nut-list">
      <li class="nut-item"><span class="nut-icon" role="img" aria-label="Peanut line icon"></span><span class="nut-name">Peanut</span></li>
      <li class="nut-item"><span class="nut-icon" role="img" aria-label="Almond line icon"></span><span class="nut-name">Almond</span></li>
      <li class="nut-item"><span class="nut-icon" role="img" aria-label="Cashew line icon"></span><span class="nut-name">Cashew</span></li>
      <li class="nut-item"><span class="nut-icon" role="img" aria-label="Macadamia line icon"></span><span class="nut-name">Macadamia</span></li>
      <li class="nut-item"><span class="nut-icon" role="img" aria-label="Hazelnut line icon"></span><span class="nut-name">Hazelnut</span></li>
      <li class="nut-item"><span class="nut-icon" role="img" aria-label="Pistachio line icon"></span><span class="nut-name">Pistachio</span></li>
    </ul>
  </section>

  <section class="panel panel--front">
    <div class="brand"><span class="brand-square"></span><span class="brand-name">CRUMB VALET</span></div>
    <div class="product-shot" role="img" aria-label="Product photo of the grey and black electric nut butter mixer with red buttons and a spiral stainless steel hook"></div>
    <div class="badges">
      <svg class="badge" viewBox="0 0 92 92" aria-label="High torque 3 speed custom motor">
        <circle cx="46" cy="46" r="42" fill="var(--teal)"/>
        <circle cx="46" cy="46" r="30" fill="var(--white)"/>
        <defs>
          <path id="arcTopA" d="M12 46 A34 34 0 0 1 80 46"/>
          <path id="arcBotA" d="M10 46 A36 36 0 0 0 82 46"/>
        </defs>
        <text font-family="Barlow Condensed, sans-serif" font-size="10" fill="var(--slate)"><textPath href="#arcTopA" startOffset="50%" text-anchor="middle">High Torque</textPath></text>
        <text font-family="Barlow Condensed, sans-serif" font-size="10" fill="var(--slate)"><textPath href="#arcBotA" startOffset="50%" text-anchor="middle" dominant-baseline="hanging">Custom Motor</textPath></text>
        <text x="46" y="52" text-anchor="middle" font-family="Barlow, sans-serif" font-weight="600" font-size="24" fill="var(--slate)">3</text>
        <text x="46" y="64" text-anchor="middle" font-family="Barlow, sans-serif" font-size="9" fill="var(--slate)">speed</text>
      </svg>
      <svg class="badge" viewBox="0 0 92 92" aria-label="Unique 2 mm stainless steel hook">
        <circle cx="46" cy="46" r="42" fill="var(--slate)"/>
        <circle cx="46" cy="46" r="30" fill="var(--white)"/>
        <defs>
          <path id="arcTopB" d="M12 46 A34 34 0 0 1 80 46"/>
          <path id="arcBotB" d="M10 46 A36 36 0 0 0 82 46"/>
        </defs>
        <text font-family="Barlow Condensed, sans-serif" font-size="10" fill="var(--white)"><textPath href="#arcTopB" startOffset="50%" text-anchor="middle">Unique Stainless</textPath></text>
        <text font-family="Barlow Condensed, sans-serif" font-size="10" fill="var(--white)"><textPath href="#arcBotB" startOffset="50%" text-anchor="middle" dominant-baseline="hanging">Steel Hook</textPath></text>
        <text x="46" y="52" text-anchor="middle" font-family="Barlow, sans-serif" font-weight="600" font-size="24" fill="var(--slate)">2</text>
        <text x="46" y="64" text-anchor="middle" font-family="Barlow, sans-serif" font-size="9" fill="var(--slate)">mm</text>
      </svg>
    </div>
    <div class="claims">
      <span class="claim">No Mess</span>
      <span class="claim">No Waste</span>
      <span class="claim">Better Taste</span>
    </div>
  </section>

  <section class="panel panel--snack">
    <div class="snack-photo" role="img" aria-label="Stock photo of toast spread with nut butter, topped with sliced red apples, flaked almonds and pomegranate seeds, with a knife on a stone counter"></div>
    <p class="serving-note">Mix once at<br>room temperature<br>then refrigerate<br>and DONE!</p>
  </section>

</main>
</body>
</html>
```